Open Horizon; Teaching Series Art.

Our church is going to be teaching a series of messages under the topic/title: Open Horizon. Just looking for a simple design to help with this. I have uploaded a design that is an example of what we were thinking.

The point of the design is to communicate a new way of doing things (given some of the impact of the coronavirus) - although the background doesn't need to be too busy - just something simple, clean and modern.

Even though it's for a church, we don't need any religious art in the background (crosses, people praying, etc.) Looking for a similar feel background to the one we uploaded.

The only text should be Open Horizon and maybe highlighting the word Open somehow.

Font styles to use
Sans Serif

Requirements
Must have
• Title of "Open Horizon" - no other text.

```html
<!DOCTYPE html>
<html lang="en">
<head>
<meta charset="utf-8">
<title>Open Horizon — Teaching Series</title>
<link rel="stylesheet" href="https://fonts.googleapis.com/css2?family=Nunito:wght@500&display=swap">
<style>
  :root {
    --teal: #17b4bd;
    --teal-light: #6fcbcc;
    --ocean: #0a87b3;
    --indigo: #4a4ca0;
    --sky: #3f7fca;
    --violet: #7a55a8;
    --magenta: #9a3b98;
    --title-blue: #0b7fae;
    --bracket-purple: #8c3795;
    --card-white: #ffffff;
  }
  * { margin: 0; padding: 0; box-sizing: border-box; }
  html, body {
    width: 1200px;
    height: 750px;
    overflow: hidden;
    background: var(--card-white);
  }
  .series-art {
    position: relative;
    width: 1200px;
    height: 750px;
    overflow: hidden;
  }
  .painted-backdrop {
    position: absolute;
    inset: 0;
    background:
      radial-gradient(ellipse 320px 260px at 300px 330px, var(--teal-light) 0%, rgba(111,203,204,0) 70%),
      radial-gradient(ellipse 420px 300px at 420px 90px, var(--ocean) 0%, rgba(10,135,179,0) 75%),
      radial-gradient(ellipse 380px 260px at 760px 120px, var(--indigo) 0%, rgba(74,76,160,0) 75%),
      radial-gradient(ellipse 320px 300px at 1080px 200px, var(--sky) 0%, rgba(63,127,202,0) 75%),
      radial-gradient(ellipse 300px 260px at 380px 560px, var(--sky) 0%, rgba(63,127,202,0) 75%),
      radial-gradient(ellipse 420px 240px at 860px 420px, var(--violet) 0%, rgba(122,85,168,0) 75%),
      radial-gradient(ellipse 620px 300px at 880px 660px, var(--magenta) 0%, rgba(154,59,152,0) 75%),
      linear-gradient(115deg, var(--teal) 0%, var(--teal) 25%, var(--sky) 50%, var(--violet) 70%, var(--magenta) 100%);
  }
  .title-plate {
    position: absolute;
    left: 364px;
    top: 315px;
    width: 474px;
    height: 120px;
    background: var(--card-white);
    display: flex;
    align-items: center;
    justify-content: center;
  }
  .series-title {
    font-family: "Nunito", "Helvetica Neue", Arial, sans-serif;
    font-weight: 500;
    font-size: 58px;
    line-height: 1;
    letter-spacing: -0.5px;
    color: var(--title-blue);
    display: flex;
    align-items: center;
    gap: 14px;
    white-space: nowrap;
  }
  .title-highlight {
    display: inline-flex;
    align-items: center;
    gap: 8px;
  }
  .bracket {
    width: 17px;
    height: 102px;
    flex: none;
  }
  .bracket path {
    fill: none;
    stroke: var(--bracket-purple);
    stroke-width: 5;
  }
  .highlight-word,
  .main-word { padding-bottom: 4px; }
</style>
</head>
<body>
  <main class="series-art">
    <div class="painted-backdrop" role="img"
         aria-label="Painted brush-stroke background blending teal, blue, indigo and magenta, with scattered virus-particle illustrations"></div>

    <div class="title-plate">
      <h1 class="series-title">
        <span class="title-highlight">
          <svg class="bracket bracket-open" viewBox="0 0 17 102" aria-hidden="true">
            <path d="M15 2.5 H2.5 V99.5 H15"/>
          </svg>
          <span class="highlight-word">Open</span>
          <svg class="bracket bracket-close" viewBox="0 0 17 102" aria-hidden="true">
            <path d="M2 2.5 H14.5 V99.5 H2"/>
          </svg>
        </span>
        <span class="main-word">Horizon</span>
      </h1>
    </div>
  </main>
</body>
</html>
```